Upmarket building and construction company needs signage

Our building company R Brent Construction, needs signage to put up on the side of our vehicle trailers and on site fencing. We are a building company that specialises in residential construction and carpentry .

I will attach our logo and some inspirational pics for site fencing as well as what our trailer looks like .
Other details i would like on the sign are our
( email) rbrentconstruction@mailbox-example.net
(mobile ) 0493 518 264
(website ) rbrentconstruction. example.net

Target Market(s)

Home owners looking for a reliable local builder who produces good quality work. I have attached some inspirational pics.

Industry/Entity Type

Building and Construction

Colors

Designer to choose colors to be used in the design.

Requirements
Must have
• Our logo, contact information
Nice to have
• We would like the design to have elements of being Elegant, Serious, Modern, Professional, Masculine, Conservative and Upmarket.

```html
<!DOCTYPE html>
<html lang="en">
<head>
<meta charset="utf-8">
<title>R Brent Construction – Site Sign</title>
<link href="https://fonts.googleapis.com/css2?family=Jost:wght@300;400&family=Marcellus&display=swap" rel="stylesheet">
<style>
  :root {
    --backdrop: #767a83;
    --sign: #ffffff;
    --brand-grey: #6e6e6e;
    --ink: #111111;
    --rule: #2a2a2a;
  }
  * { margin: 0; padding: 0; box-sizing: border-box; }
  html, body {
    width: 850px;
    height: 1200px;
    overflow: hidden;
    background: var(--backdrop);
  }
  .canvas {
    position: relative;
    width: 850px;
    height: 1200px;
    display: flex;
    align-items: center;
    justify-content: center;
  }
  .sign {
    width: 760px;
    height: 552px;
    background: var(--sign);
    display: flex;
    flex-direction: column;
  }
  .brand {
    flex: 1;
    display: flex;
    flex-direction: column;
    align-items: center;
    justify-content: flex-end;
    padding-bottom: 34px;
  }
  .brand-name {
    font-family: "Jost", sans-serif;
    font-weight: 300;
    color: var(--brand-grey);
    font-size: 62px;
    line-height: 1.05;
    letter-spacing: 0.06em;
    text-transform: uppercase;
    text-align: center;
  }
  .brand-tagline {
    margin-top: 22px;
    font-family: "Jost", sans-serif;
    font-weight: 300;
    color: var(--brand-grey);
    font-size: 27px;
    letter-spacing: 0.09em;
    text-transform: uppercase;
  }
  .contact-bar {
    height: 122px;
    border-top: 1px solid var(--rule);
    display: flex;
    align-items: center;
    padding: 0 26px 0 34px;
  }
  .phone {
    font-family: "Marcellus", serif;
    color: var(--ink);
    font-size: 46px;
    letter-spacing: 0.01em;
    white-space: nowrap;
  }
  .divider {
    width: 1px;
    height: 54px;
    background: var(--rule);
    margin: 0 22px 0 28px;
  }
  .contact-list {
    list-style: none;
    font-family: "Marcellus", serif;
    color: var(--ink);
    font-size: 16.5px;
    line-height: 1.65;
  }
  .contact-list li {
    display: flex;
    align-items: center;
    gap: 9px;
    white-space: nowrap;
  }
  .contact-list svg {
    width: 14px;
    height: 14px;
    flex: none;
  }
</style>
</head>
<body>
<main class="canvas">
  <section class="sign">
    <div class="brand">
      <h1 class="brand-name">R Brent<br>Construction</h1>
      <p class="brand-tagline">Building and Carpentry</p>
    </div>
    <div class="contact-bar">
      <span class="phone">0493 518 264</span>
      <span class="divider"></span>
      <ul class="contact-list">
        <li>
          <svg viewBox="0 0 16 16" aria-hidden="true" fill="none" stroke="#222" stroke-width="1">
            <rect x="1" y="3.5" width="14" height="9"/>
            <path d="M1 3.5 L8 9 L15 3.5 M1 12.5 L6 7.5 M15 12.5 L10 7.5"/>
          </svg>
          rbrentconstruction@mailbox-example.net
        </li>
        <li>
          <svg viewBox="0 0 16 16" aria-hidden="true" fill="none" stroke="#222" stroke-width="1">
            <circle cx="8" cy="8" r="6.5"/>
            <ellipse cx="8" cy="8" rx="3" ry="6.5"/>
            <path d="M1.5 8 H14.5 M2.5 4.8 H13.5 M2.5 11.2 H13.5"/>
          </svg>
          rbrentconstruction. example.net
        </li>
      </ul>
    </div>
  </section>
</main>
</body>
</html>
```